Trailbound Hub Outfitter Directory

Hero Section
Image: A serene and picturesque camping landscape with a lake, mountains, and a few trees There is a circle of people sitting around a campfire. The image should be high-quality and visually appealing.
Headline: "Introducing Trailboundhub.com's Outfitter Directory"
Subheading: "Join our directory of trusted outfitters and reach a targeted audience of camping enthusiasts."
Call-to-Action (CTA) Button: "Learn More" or "Join Now"
Color scheme: Match trailboundhub.com and the logo
Example:
[Image: A serene and picturesque camping landscape with a lake, mountains, and a few trees]
Introducing Trailboundhub.com's Outfitter Directory
Join our directory of trusted outfitters and reach a targeted audience of camping enthusiasts.
Learn More
Benefits Section
Image: A group of happy campers sitting around a campfire, roasting marshmallows and telling stories.
Headline: "Benefits of Joining Our Directory"
Bullet points:
"Increase your exposure and visibility to potential customers"
"Book more trips and generate more revenue"
"Access a targeted audience of camping enthusiasts"
Color scheme: match trailboundhub.com
Example:
[Image: A group of happy campers sitting around a campfire, roasting marshmallows and telling stories]
Benefits of Joining Our Directory
• Increase your exposure and visibility to potential customers • Book more trips and generate more revenue • Access a targeted audience of camping enthusiasts
Features Section
Image: A screenshot of the directory's search functionality, showing a list of outfitters with their logos, names, and locations.
Headline: "Features of Our Outfitter Directory"
Bullet points:
"Search functionality to find outfitters by location, activity, or type"
"Outfitter profiles with detailed information and reviews"
"Booking system to make it easy for customers to book trips"
Example:
[Image: A screenshot of the directory's search functionality, showing a list of outfitters with their logos, names, and locations]
Features of Our Outfitter Directory
• Search functionality to find outfitters by location, activity, or type • Outfitter profiles with detailed information and reviews • Booking system to make it easy for customers to book trips
CTA Section
Image: A simple and clean design with a prominent call-to-action button.
Headline: "Express Interest in Joining Our Directory"
Call-to-Action (CTA) Button: "Express Interest" or "Join Now"

Example:
[Image: A simple and clean design with a prominent call-to-action button]
Express Interest in Joining Our Directory
Express Interest
Contact Information Section
Image: A simple and clean design with a form to collect contact information.
Headline: "Get in Touch with Us"
Form fields:
Name
Email
Phone
Website

```html
<!DOCTYPE html>
<html lang="en">
<head>
<meta charset="utf-8">
<title>Trailbound Hub – Outfitter Directory</title>
<link href="https://fonts.googleapis.com/css2?family=Roboto:wght@400;500;700;900&family=Roboto+Condensed:wght@700&display=swap" rel="stylesheet">
<style>
:root{
  --orange:#ff5a14;
  --orange-soft:#fcd3c0;
  --ink:#111111;
  --text:#222222;
  --muted:#9a9a9a;
  --line:#e3e3e3;
  --white:#ffffff;
  --footer:#1f1f1f;
  --laptop:#2a2a2a;
}
*{margin:0;padding:0;box-sizing:border-box}
html,body{width:1200px;height:3217px;overflow:hidden}
body{position:relative;font-family:'Roboto',sans-serif;color:var(--text);background:var(--white)}
.abs{position:absolute}
.btn{position:absolute;display:flex;align-items:center;justify-content:center;gap:14px;background:var(--orange);color:var(--white);font-weight:700;border-radius:40px;text-decoration:none}
.btn svg{width:32px;height:14px}
.accent-bar{position:absolute;height:4px;background:var(--orange);border-radius:2px}

/* hero */
.hero{position:absolute;left:0;top:0;width:1200px;height:693px;
  background:linear-gradient(180deg,#e9a879 0%,#d98c62 22%,#8b6a76 45%,#4e3c4a 70%,#2a2226 100%)}
.brand-badge{position:absolute;width:132px;height:132px;border-radius:50%;background:var(--white);display:flex;align-items:center;justify-content:center;text-align:center;
  font-weight:700;font-size:19px;line-height:1.1;color:#1d3a4a}
.hero-kicker{position:absolute;left:0;width:1200px;top:274px;text-align:center;font-family:'Roboto Condensed',sans-serif;font-size:45px;color:var(--white)}
.hero-title{position:absolute;left:0;width:1200px;top:316px;text-align:center;font-family:'Roboto Condensed',sans-serif;font-size:80px;color:var(--white);line-height:1.1}
.hero-sub{position:absolute;left:0;width:1140px;top:414px;text-align:center;font-size:21px;line-height:25px;color:var(--white)}

/* benefits */
.benefits{position:absolute;left:0;top:693px;width:1200px;height:508px;background:linear-gradient(180deg,#e4e7ec 0%,#eceef1 50%,#dfe1e4 100%)}
.section-title{position:absolute;font-weight:700;font-size:37px;line-height:44px;color:var(--ink)}
.point{position:absolute;display:flex;align-items:center}
.point .icon{position:absolute;width:40px;height:40px}
.point p{font-size:17px;line-height:20px;color:var(--text)}
.divider{position:absolute;height:1px;background:var(--line)}

/* features */
.laptop-screen{position:absolute;left:586px;top:1336px;width:469px;height:315px;background:var(--laptop);border-radius:12px 12px 0 0}
.laptop-display{position:absolute;left:603px;top:1357px;width:435px;height:274px;background:var(--white)}
.laptop-base{position:absolute;left:532px;top:1651px;width:576px;height:16px;background:linear-gradient(180deg,#f1f1f1,#c9c9c9);border-radius:0 0 30px 30px;box-shadow:0 22px 30px rgba(0,0,0,.08)}
.listing{position:absolute;left:603px;width:435px;height:68px;border-bottom:1px solid var(--line)}
.listing .avatar{position:absolute;left:24px;top:8px;width:52px;height:52px;border-radius:50%;background:linear-gradient(135deg,#8a7a6a,#3d4a55)}
.listing .name{position:absolute;left:83px;top:18px;font-size:14px;line-height:16px;color:var(--orange)}
.listing .role{position:absolute;left:83px;top:34px;font-size:14px;line-height:16px;color:var(--text)}
.listing .place{position:absolute;left:239px;top:26px;font-size:14px;color:var(--text)}
.listing .logo-slot{position:absolute;left:330px;top:27px;font-size:12px;font-weight:700;color:var(--muted)}

/* cta */
.cta{position:absolute;left:0;top:1804px;width:1200px;height:529px;background:linear-gradient(90deg,#3b3a2c 0%,#4a5a3a 40%,#5d6e4f 70%,#3f5234 100%)}
.cta-title{position:absolute;left:578px;top:1962px;font-weight:700;font-size:55px;line-height:62px;color:var(--white)}

/* contact */
.contact-bg{position:absolute;left:0;top:2560px;width:1200px;height:400px;background:linear-gradient(180deg,#ffffff 0%,#e8c9a0 35%,#c58a3c 65%,#4d5a2c 100%)}
.field{position:absolute;left:363px;width:474px;height:55px;border:1px solid #cfcfcf;border-radius:28px;background:var(--white);padding-left:22px;display:flex;align-items:center;font-size:15px;color:var(--text)}

/* footer */
.footer{position:absolute;left:0;top:2960px;width:1200px;height:257px;background:var(--footer)}
.copyright{position:absolute;left:0;width:1200px;top:3082px;text-align:center;font-size:15px;color:#dddddd}
.footer-links{position:absolute;left:0;width:1200px;top:3121px;text-align:center;font-size:15px;color:#bdbdbd;word-spacing:2px}
.footer-links span{margin:0 18px}
</style>
</head>
<body>

<section class="hero" role="img" aria-label="Sunset over a misty mountain range"></section>
<div class="brand-badge" style="left:534px;top:44px">Trailbound<br>Hub</div>
<div class="hero-kicker">Introducing Trailboundhub.com's</div>
<h1 class="hero-title">Outfitter Directory</h1>
<p class="hero-sub">Join our directory of trusted outfitters and reach a<br>targeted audience of camping enthusiasts.</p>
<a class="btn" style="left:513px;top:504px;width:174px;height:60px;font-size:19px">Join Now
  <svg viewBox="0 0 32 14" fill="none" stroke="#fff" stroke-width="2"><path d="M0 7h30M24 1l6 6-6 6"/></svg></a>

<section class="benefits" role="img" aria-label="Soft hazy sky over distant hills"></section>
<div class="abs" style="left:343px;top:777px;width:150px;height:150px;border-radius:50%;background:var(--orange)"></div>
<svg class="abs" style="left:189px;top:785px" width="410" height="362" viewBox="0 0 410 362" role="img" aria-label="Friends sitting around a campfire at night beside a tent">
  <defs><linearGradient id="fire" x1="0" y1="0" x2="0" y2="1"><stop offset="0" stop-color="#2c3440"/><stop offset=".6" stop-color="#4a3526"/><stop offset="1" stop-color="#b8692a"/></linearGradient></defs>
  <path d="M90 4C160-10 250 70 330 58 390 50 415 110 408 170 400 260 330 350 210 360 90 368 5 300 1 170-2 80 30 16 90 4Z" fill="url(#fire)"/>
</svg>
<div class="accent-bar" style="left:666px;top:771px;width:81px"></div>
<h2 class="section-title" style="left:666px;top:778px">Benefits of Joining<br>Our Directory</h2>
<div class="point" style="left:713px;top:900px"><svg class="icon" style="left:-48px" viewBox="0 0 40 40" fill="none" stroke="#ff5a14" stroke-width="1.6"><path d="M4 36h34M7 36v-8h5v8M15 36v-12h5v12M23 36v-16h5v16M31 36v-21h5v21M4 22L30 6M24 5h6v6"/></svg><p>Increase your exposure and visibility<br>to potential customers</p></div>
<div class="divider" style="left:713px;top:959px;width:274px"></div>
<div class="point" style="left:713px;top:980px"><svg class="icon" style="left:-48px" viewBox="0 0 40 40" fill="none" stroke="#ff5a14" stroke-width="1.6"><rect x="3" y="6" width="28" height="26" rx="2"/><path d="M3 13h28M10 3v6M24 3v6M8 18h4M15 18h4M8 24h4M15 24h4"/><circle cx="30" cy="30" r="7" fill="#fff"/><path d="M30 26v4l3 2"/></svg><p>Book more trips and generate more<br>revenue</p></div>
<div class="divider" style="left:713px;top:1041px;width:274px"></div>
<div class="point" style="left:713px;top:1061px"><svg class="icon" style="left:-48px" viewBox="0 0 40 40" fill="none" stroke="#ff5a14" stroke-width="1.6"><path d="M4 36h34M12 36l10-18 10 18M22 18v18M6 36V24M3 28l3-6 3 6M28 8a4 4 0 1 0 4 4 3 3 0 0 1-4-4"/></svg><p>Access a targeted audience of<br>camping enthusiasts</p></div>

<div class="abs" style="left:849px;top:1270px;width:320px;height:320px;border-radius:50%;background:var(--orange-soft)"></div>
<div class="accent-bar" style="left:129px;top:1332px;width:80px"></div>
<h2 class="section-title" style="left:129px;top:1339px">Features of Our<br>Outfitter Directory</h2>
<div class="point" style="left:184px;top:1460px"><svg class="icon" style="left:-56px" viewBox="0 0 40 40" fill="none" stroke="#ff5a14" stroke-width="1.6"><rect x="5" y="3" width="24" height="32" rx="2"/><path d="M10 10h14M10 15h8"/><circle cx="22" cy="24" r="8" fill="#fff"/><path d="M19 22h6M19 26h6M28 30l6 6"/></svg><p>Search functionality to find outfitters<br>by location, activity, or type</p></div>
<div class="divider" style="left:184px;top:1522px;width:273px"></div>
<div class="point" style="left:184px;top:1541px"><svg class="icon" style="left:-56px" viewBox="0 0 40 40" fill="none" stroke="#ff5a14" stroke-width="1.6"><circle cx="20" cy="6" r="3"/><path d="M18 11l-4 12 6 4 2 10M16 18l-6 4v15M18 12l7 6 5-1M30 14v24"/><rect x="8" y="12" width="6" height="10" rx="2"/></svg><p>Outfitter profiles with detailed<br>information and reviews</p></div>
<div class="divider" style="left:184px;top:1605px;width:273px"></div>
<div class="point" style="left:184px;top:1621px"><svg class="icon" style="left:-56px" viewBox="0 0 40 40" fill="none" stroke="#ff5a14" stroke-width="1.6"><rect x="3" y="6" width="28" height="26" rx="2"/><path d="M3 13h28M10 3v6M24 3v6M8 18h4M15 18h4M8 24h4M15 24h4"/><circle cx="30" cy="30" r="7" fill="#fff"/><path d="M30 26v4l3 2"/></svg><p>Booking system to make it easy for<br>customers to book trips</p></div>

<div class="laptop-screen"></div>
<div class="abs" style="left:817px;top:1344px;width:6px;height:6px;border-radius:50%;background:#444"></div>
<div class="laptop-display"></div>
<div class="listing" style="top:1357px"><div class="avatar" role="img" aria-label="Outfitter profile photo"></div><div class="name">Mara Ellison</div><div class="role">Placeholder</div><div class="place">Florida</div><div class="logo-slot">LOGO HERE</div></div>
<div class="listing" style="top:1425px"><div class="avatar" role="img" aria-label="Outfitter profile photo"></div><div class="name">Mara Ellison</div><div class="role">Placeholder</div><div class="place">Canada</div><div class="logo-slot">LOGO HERE</div></div>
<div class="listing" style="top:1494px"><div class="avatar" role="img" aria-label="Outfitter profile photo"></div><div class="name">Mara Ellison</div><div class="role">Placeholder</div><div class="place">Florida</div><div class="logo-slot">LOGO HERE</div></div>
<div class="listing" style="top:1562px;border-bottom:0"><div class="avatar" role="img" aria-label="Outfitter profile photo"></div><div class="name">Mara Ellison</div><div class="role">Placeholder</div><div class="place">USA</div><div class="logo-slot">LOGO HERE</div></div>
<div class="laptop-base"></div>

<section class="cta" role="img" aria-label="Hiker with a backpack and trekking poles overlooking a forested river valley"></section>
<h2 class="cta-title">Express Interest in<br>Joining Our Directory</h2>
<a class="btn" style="left:578px;top:2120px;width:270px;height:60px;font-size:21px">Express Interest
  <svg viewBox="0 0 32 14" fill="none" stroke="#fff" stroke-width="2"><path d="M0 7h30M24 1l6 6-6 6"/></svg></a>

<div class="contact-bg" role="img" aria-label="Sunlit pine forest below misty mountain peaks"></div>
<div class="accent-bar" style="left:561px;top:2411px;width:78px"></div>
<h2 class="section-title" style="left:0;width:1200px;top:2419px;text-align:center">Get in Touch with Us</h2>
<div class="field" style="top:2481px">Name:</div>
<div class="field" style="top:2545px">Email</div>
<div class="field" style="top:2607px">Phone</div>
<div class="field" style="top:2671px">Website</div>
<a class="btn" style="left:363px;top:2733px;width:474px;height:53px;font-size:20px">Submit Now
  <svg viewBox="0 0 32 14" fill="none" stroke="#fff" stroke-width="2"><path d="M0 7h30M24 1l6 6-6 6"/></svg></a>

<footer class="footer"></footer>
<div class="brand-badge" style="left:534px;top:2898px;border:4px solid var(--footer)">Trailbound<br>Hub</div>
<p class="copyright">© 2024 All Rights are Reserved. Trailbound Hub.</p>
<p class="footer-links">Refund Policy<span>|</span>Privacy Policy<span>|</span>Terms of Service</p>

</body>
</html>
```